Cell Tower company needs website updated

We need a website that does not look like it was designed in the early 1990's. The company fabricates, installs and reinforces communication towers throughout the US, Caribbean, Central and S. America. We are located in Pensacola Florida. Our tower technicians travel to wherever the work is. I have some good pictures taken from towers to use on the site. I want the site to reflect the excitement that the wireless communication industry has. I want to the company to look exciting and attract new employees. The majority of our business is modifying and reinforcing existing cell towers to accept all the new tower top antennas that the increasing wireless mobile world demands.
Updates

I have added some sample photos from our business to our ArtBazaar profile.

We are now going through each design to find what is most suitable for our needs. Thank you all for your time in this matter.

Industry/Entity Type

Wireless Communication

```html
<!DOCTYPE html>
<html lang="en">
<head>
<meta charset="utf-8">
<title>SpireWorks — Towering Above the Rest</title>
<link href="https://fonts.googleapis.com/css2?family=Roboto:wght@300;400;500&family=Roboto+Slab:wght@400;700&display=swap" rel="stylesheet">
<style>
:root{
  --red:#c8232c;
  --red-deep:#8e1119;
  --bar:#a71d2f;
  --ink:#2b2b2b;
  --muted:#8798ae;
  --grey:#6b6b6b;
  --paper:#ffffff;
  --ground:#f2f2f2;
}
*{box-sizing:border-box;margin:0;padding:0}
html,body{width:1024px;height:1200px;overflow:hidden}
body{position:relative;background:var(--ground);font-family:"Roboto",sans-serif;color:var(--ink)}
.abs{position:absolute}
.hero{left:0;top:0;width:1024px;height:482px;background:radial-gradient(ellipse at 45% 35%,#f0454a 0%,#c8232c 45%,#7d1016 100%)}
.worker-photo{left:152px;top:105px;width:288px;height:263px;background:linear-gradient(160deg,#d9a64a 0%,#4b5f86 55%,#b78a4a 100%);opacity:.85}
.tower-photo{left:440px;top:105px;width:584px;height:377px;background:linear-gradient(180deg,rgba(90,10,15,.25),rgba(90,10,15,.45))}
.header{left:138px;top:0;width:752px;height:105px;background:var(--paper)}
.logo{left:24px;top:38px;display:flex;align-items:center;gap:8px;font-size:30px;font-weight:400;color:var(--ink);white-space:nowrap}
.logo-dot{width:14px;height:14px;border-radius:50%;background:var(--red)}
.top-contact{top:15px;display:flex;align-items:center;gap:6px;font-size:10.5px;color:var(--grey);white-space:nowrap}
.nav{top:70px;font-family:"Roboto Slab",serif;font-size:14px;font-weight:400;color:#333;letter-spacing:.3px;white-space:nowrap}
.nav.active{color:var(--red)}
.nav-line{left:706px;top:101px;width:60px;height:3px;background:var(--red)}
.hero-kicker{left:502px;top:179px;font-size:14px;font-weight:500;color:#f0a5a5;letter-spacing:-.2px;white-space:nowrap}
.hero-title{left:502px;top:194px;font-family:"Roboto Slab",serif;font-weight:700;font-size:38px;line-height:47px;color:#fff;letter-spacing:.5px;white-space:nowrap}
.panel{left:138px;top:368px;width:752px;height:646px;background:var(--paper);box-shadow:0 1px 3px rgba(0,0,0,.15)}
.col-title{top:21px;width:215px;text-align:center;font-size:14.5px;font-weight:400;color:var(--ink)}
.col-img{top:50px;width:215px;height:71px;border-radius:3px}
.col-text{top:138px;width:215px;font-size:10.5px;line-height:16px;color:var(--muted)}
.col-list{top:138px;list-style:none;font-size:10.5px;line-height:24px;color:var(--muted);white-space:nowrap}
.col-list li::before{content:"";display:inline-block;border-left:4px solid var(--red-deep);border-top:3.5px solid transparent;border-bottom:3.5px solid transparent;margin:0 9px 0 6px}
.btn{top:215px;width:64px;height:28px;border-radius:3px;background:linear-gradient(#6d6d6d,#444);color:#fff;font-size:9px;display:flex;align-items:center;justify-content:center;box-shadow:0 0 0 1px #333 inset}
.rule{left:22px;top:274px;width:704px;height:4px;border-top:1px dotted #bbb;border-bottom:1px dotted #bbb}
.section-title{left:0;top:293px;width:752px;text-align:center;font-size:15px;font-weight:400;color:var(--ink)}
.card-img{width:166px;height:87px}
.card-title{font-size:13.5px;font-weight:300;color:#333;white-space:nowrap}
.card-more{font-size:8.5px;color:#999;white-space:nowrap}
.footer-logo{left:146px;top:1058px;display:flex;align-items:center;gap:6px;font-size:21px;color:var(--ink)}
.footer-logo .logo-dot{width:10px;height:10px}
.f-head{top:1045px;font-size:15px;font-weight:300;color:#444}
.f-link{font-size:10.5px;color:#999;white-space:nowrap}
.f-link::before{content:"";display:inline-block;border-left:3px solid #777;border-top:3px solid transparent;border-bottom:3px solid transparent;margin-right:6px;vertical-align:1px}
.f-info{left:536px;font-size:10.5px;color:#999;line-height:16px;white-space:nowrap}
.f-icon{left:518px}
.social{top:1080px;width:26px;height:26px}
.bottom-bar{left:0;top:1176px;width:1024px;height:24px;background:var(--bar);color:#fff;font-size:9px}
.bottom-bar span{white-space:nowrap}
</style>
</head>
<body>
<div class="abs hero" role="img" aria-label="Red sky over steel transmission towers"></div>
<div class="abs tower-photo" role="img" aria-label="Silhouettes of power transmission towers"></div>
<div class="abs worker-photo" role="img" aria-label="Smiling tower technician in hard hat carrying a coiled yellow cable"></div>

<header class="abs header">
  <div class="abs logo"><span>SpireWorks</span><span class="logo-dot"></span></div>
  <div class="abs top-contact" style="left:468px">
    <svg width="18" height="12" viewBox="0 0 18 12"><rect x="5" y="1" width="12" height="10" fill="none" stroke="#c8232c" stroke-width="1.4"/><path d="M5 1l6 5 6-5" fill="none" stroke="#c8232c" stroke-width="1.4"/><path d="M0 3h4M1 6h3M0 9h4" stroke="#c8232c"/></svg>
    <span>info@spireworks.com</span>
  </div>
  <div class="abs top-contact" style="left:630px">
    <svg width="14" height="14" viewBox="0 0 14 14"><path d="M3 1l2 3-1.5 1.5c1 2 3 4 5 5L10 9l3 2-1.5 2.5C6 13 1 8 .5 2.5z" fill="#c8232c"/></svg>
    <span>+1 850 555 0142</span>
  </div>
  <span class="abs nav" style="left:390px">HOME</span>
  <span class="abs nav" style="left:465px">ABOUT US</span>
  <span class="abs nav active" style="left:568px">SERVICES</span>
  <span class="abs nav" style="left:664px">CONTACT</span>
</header>
<div class="abs nav-line"></div>

<div class="abs hero-kicker">REINFORCING FOR THE FUTURE</div>
<div class="abs hero-title">TOWERING<br>ABOVE THE REST</div>

<main class="abs panel">
  <h2 class="abs col-title" style="left:22px">About SpireWorks</h2>
  <div class="abs col-img" style="left:22px;background:linear-gradient(90deg,#777,#c9c9c9)" role="img" aria-label="Climber on a lattice tower, black and white"></div>
  <p class="abs col-text" style="left:22px">Mauris placerat placerat felis, non tincidunt sem pretium eget. Aliquam lacinia nisi vel mi ultricies accumsan. Quisque auctor faucibus ornare.</p>
  <div class="abs btn" style="left:22px">Learn More</div>

  <h2 class="abs col-title" style="left:264px">What We Offer</h2>
  <div class="abs col-img" style="left:264px;background:linear-gradient(90deg,#333,#999 60%,#444)" role="img" aria-label="Welder at work, black and white"></div>
  <ul class="abs col-list" style="left:264px">
    <li>Many years of Reinforcing Experience</li>
    <li>Vendor to all Major Carriers and Owners</li>
    <li>State of the Art Manufacturing Plant</li>
  </ul>
  <div class="abs btn" style="left:264px">Learn More</div>

  <h2 class="abs col-title" style="left:511px">Careers</h2>
  <div class="abs col-img" style="left:511px;background:linear-gradient(180deg,#fff 10%,#8a8a8a 90%)" role="img" aria-label="Group of five team members, black and white"></div>
  <p class="abs col-text" style="left:511px">Mauris placerat placerat felis, non tincidunt sem pretium eget. Aliquam lacinia nisi vel mi ultricies accumsan. Quisque auctor faucibus ornare.</p>
  <div class="abs btn" style="left:511px">Apply Now</div>

  <div class="abs rule"></div>
  <h2 class="abs section-title">Products and Services</h2>

  <div class="abs card-img" style="left:21px;top:330px;background:linear-gradient(135deg,#5a6a7a,#b8c0c8)" role="img" aria-label="Steel tower joint"></div>
  <div class="abs card-title" style="left:19px;top:428px">Tower Reinforcement</div>
  <div class="abs card-more" style="left:21px;top:451px">Learn More »</div>

  <div class="abs card-img" style="left:202px;top:330px;background:linear-gradient(180deg,#8fb0cc,#7a8a6a 70%,#c0c0c0)" role="img" aria-label="Rapid deployment site on a hillside"></div>
  <div class="abs card-title" style="left:200px;top:427px">Rapid Deployment Site</div>
  <div class="abs card-more" style="left:202px;top:451px">Learn More »</div>

  <div class="abs card-img" style="left:382px;top:330px;background:linear-gradient(180deg,#3f6fbf,#2a5cae)" role="img" aria-label="Towers against blue sky"></div>
  <div class="abs card-title" style="left:381px;top:427px">Towers</div>
  <div class="abs card-more" style="left:383px;top:451px">Learn More »</div>

  <div class="abs card-img" style="left:563px;top:330px;background:linear-gradient(90deg,#4a6a3a,#6fa0d8 40%,#8fb8e8)" role="img" aria-label="Monopole beside trees"></div>
  <div class="abs card-title" style="left:562px;top:427px">Monopole Reinforcement</div>
  <div class="abs card-more" style="left:564px;top:451px">Learn More »</div>

  <div class="abs card-img" style="left:21px;top:485px;background:linear-gradient(90deg,#fafafa,#e4e4e4)" role="img" aria-label="Tower antenna mounting bracket"></div>
  <div class="abs card-title" style="left:19px;top:583px">Tower Accessories</div>
  <div class="abs card-more" style="left:21px;top:606px">Learn More »</div>

  <div class="abs card-img" style="left:202px;top:485px;background:linear-gradient(180deg,#3b78c4,#2f6cb8)" role="img" aria-label="Antenna array on a tower top"></div>
  <div class="abs card-title" style="left:200px;top:582px">Antenna Support Structures</div>
  <div class="abs card-more" style="left:202px;top:606px">Learn More »</div>

  <div class="abs card-img" style="left:382px;top:485px;background:linear-gradient(135deg,#6b4a30,#b07040 50%,#3a2a20)" role="img" aria-label="Worker in a steel fabrication shop"></div>
  <div class="abs card-title" style="left:381px;top:582px">Custom Steel Fabrication</div>
  <div class="abs card-more" style="left:383px;top:606px">Learn More »</div>

  <div class="abs card-img" style="left:563px;top:485px;background:linear-gradient(90deg,#2a3040,#8a9098 60%,#b0b8c0)" role="img" aria-label="Technician welding on a structure"></div>
  <div class="abs card-title" style="left:562px;top:582px">Construction Services</div>
  <div class="abs card-more" style="left:564px;top:606px">Learn More »</div>
</main>

<footer>
  <div class="abs footer-logo"><span>SpireWorks</span><span class="logo-dot"></span></div>

  <h3 class="abs f-head" style="left:324px">Quick Links</h3>
  <span class="abs f-link" style="left:324px;top:1078px">Link Menu</span>
  <span class="abs f-link" style="left:407px;top:1078px">Link Menu</span>
  <span class="abs f-link" style="left:324px;top:1102px">Link Menu</span>
  <span class="abs f-link" style="left:407px;top:1102px">Link Menu</span>
  <span class="abs f-link" style="left:324px;top:1126px">Link Menu</span>
  <span class="abs f-link" style="left:407px;top:1126px">Link Menu</span>

  <h3 class="abs f-head" style="left:515px">Contact Info</h3>
  <svg class="abs f-icon" style="top:1080px" width="10" height="10" viewBox="0 0 14 14"><path d="M3 1l2 3-1.5 1.5c1 2 3 4 5 5L10 9l3 2-1.5 2.5C6 13 1 8 .5 2.5z" fill="#999"/></svg>
  <span class="abs f-info" style="top:1077px">(850) 555-0199</span>
  <svg class="abs f-icon" style="top:1104px" width="11" height="9" viewBox="0 0 11 9"><rect x=".5" y=".5" width="10" height="8" fill="none" stroke="#999"/><path d="M.5 .5l5 4 5-4" fill="none" stroke="#999"/></svg>
  <span class="abs f-info" style="top:1101px">office@spireworks.com</span>
  <svg class="abs f-icon" style="top:1128px" width="11" height="10" viewBox="0 0 11 10"><path d="M5.5 0L11 5H9.5v5h-3V7h-2v3h-3V5H0z" fill="#999"/></svg>
  <span class="abs f-info" style="top:1125px">31 Your Street, Your Ave.<br>Your State, FL 32502</span>

  <h3 class="abs f-head" style="left:710px">Social</h3>
  <div class="abs social" style="left:710px;background:#3b5a9a" role="img" aria-label="Social network link"></div>
  <div class="abs social" style="left:749px;background:#2aa8e0" role="img" aria-label="Social network link"></div>
  <div class="abs social" style="left:787px;background:#1a7bb9" role="img" aria-label="Social network link"></div>
  <div class="abs social" style="left:826px;background:#f08a24" role="img" aria-label="News feed link"></div>

  <div class="abs bottom-bar">
    <span class="abs" style="left:132px;top:7px">Copyright © 2014 All Rights Reserved by Company Name.</span>
    <span class="abs" style="left:781px;top:7px">Privacy Policy &nbsp;|&nbsp; Sitemap</span>
  </div>
</footer>
</body>
</html>
```